New homepage design - Cobalt Sages

- we would like to have a new website layout of the existing one: www.cobaltsages.ch
the new layout should have the following parameters:
- we want it to be minimalistic
- clear lines
- not too colourful (eventually also more in grey tone?)

our company: cobalt sages
- cobalt sages is an organizational consulting company and we work with organizations and individuals alike
- we are headquartered in the engadine
- examples: www.pelmartine.nyc, www.trodwickandhale.com, www.femorasix.com, www.daryluntley.website,

Target Market(s)

Companies

Industry/Entity Type

Consulting

Number of Pages Required

1 page

Font styles to use
Sans Serif

Colors

Designer to choose only greyscale colors for use in the design.

Requirements
Must have
• A minimalistic design
Nice to have
• minimalistic and slick
Should not have
• not too many colours

```html
<!DOCTYPE html>
<html lang="en">
<head>
<meta charset="utf-8">
<title>Cobalt Sages – Turn Growth Into Thriving</title>
<link href="https://fonts.googleapis.com/css2?family=DM+Sans:wght@400;500;700&display=swap" rel="stylesheet">
<style>
:root{
  --ink:#111;
  --text:#222;
  --muted:#9a9a9a;
  --hero-bg:#f2f2f2;
  --page:#fff;
  --footer-bg:#dcdcdc;
  --bar-bg:#b4b4b4;
  --rule:#9c9c9c;
  --dot:#c9c9c9;
  --dot-active:#9fd39a;
}
*{box-sizing:border-box;margin:0;padding:0}
html,body{width:1200px;height:4553px;overflow:hidden}
body{position:relative;background:var(--page);font-family:"DM Sans",Arial,sans-serif;color:var(--text)}
.abs{position:absolute}
.hero{left:0;top:0;width:1200px;height:709px;background:var(--hero-bg)}
.brand{left:127px;top:56px;text-align:center;width:140px}
.brand-name{font-size:19px;letter-spacing:.5px;color:var(--text);font-weight:400;display:flex;align-items:center;justify-content:center;gap:6px}
.brand-mark{width:9px;height:9px;background:var(--text)}
.brand-tag{font-size:7px;letter-spacing:1.2px;color:var(--muted);margin-top:3px}
.nav a{position:absolute;top:43px;font-size:12px;color:var(--text);text-decoration:none}
.btn-contact{left:967px;top:34px;width:111px;height:33px;border:1.5px solid var(--text);border-radius:17px;font-size:12px;display:flex;align-items:center;justify-content:center}
.photo{display:block}
.hero-title{left:203px;top:160px;font-size:80px;line-height:103px;font-weight:500;color:var(--ink);letter-spacing:-.5px}
.scroll{left:203px;top:584px;font-size:11px;font-weight:500}
.h-sub{font-size:39px;font-weight:400;color:var(--ink)}
.body-s{font-size:12.5px;line-height:20.5px}
.body-m{font-size:15px;line-height:21px}
.num{font-size:56px;font-weight:400;color:var(--muted);line-height:1}
.more{font-size:12px;display:flex;align-items:center;gap:10px}
.h-big{font-size:62px;line-height:71px;font-weight:400;color:var(--ink)}
.rule{left:133px;top:3509px;width:934px;height:2px;background:var(--rule)}
.card-title{font-size:21px;font-weight:700;line-height:24px;color:var(--ink)}
.card-date{font-size:12.5px;margin-top:10px}
.card-text{font-size:11.5px;line-height:14px;margin-top:16px}
.footer{left:0;top:4140px;width:1200px;height:371px;background:var(--footer-bg)}
.bar{left:0;top:4511px;width:1200px;height:42px;background:var(--bar-bg);color:#fff;font-size:13px;display:flex;align-items:center;justify-content:center}
.foot-col{font-size:12.5px;line-height:17.5px}
</style>
</head>
<body>
<div class="abs hero"></div>

<div class="abs brand">
  <div class="brand-name"><span class="brand-mark"></span>COBALT SAGES</div>
  <div class="brand-tag">TURN GROWTH INTO THRIVING</div>
</div>
<nav class="nav">
  <a style="left:353px">Cobalt Sages</a>
  <a style="left:472px">Executive Circles</a>
  <a style="left:622px">For Corporations</a>
  <a style="left:770px">For Individuals</a>
</nav>
<div class="abs btn-contact">Get in touch</div>

<div class="abs photo" role="img" aria-label="Misty fjord with a hiker standing on a rock ledge" style="left:380px;top:194px;width:542px;height:407px;background:linear-gradient(160deg,#e6e9ea 0%,#b9c3c7 40%,#7d8d93 70%,#3c4446 100%)"></div>
<h1 class="abs hero-title">Turn Growth<br>Into Thriving</h1>
<div class="abs scroll">Scroll</div>
<svg class="abs" style="left:211px;top:614px" width="14" height="18" viewBox="0 0 14 18"><path d="M7 1v15M1.5 10.5 7 16l5.5-5.5" fill="none" stroke="#111" stroke-width="1.4"/></svg>

<h2 class="abs h-sub" style="left:203px;top:780px">Cobalt Sages</h2>
<div class="abs photo" role="img" aria-label="Misty fjord landscape with a hiker on a cliff" style="left:203px;top:852px;width:228px;height:153px;background:linear-gradient(160deg,#e4e7e8,#9ea8ab 55%,#4d5557)"></div>
<div class="abs body-s" style="left:523px;top:781px;width:470px">
  <p>We convert the speak of purpose and consciousness into solutions. We are deeply convinced that a life and work ethics based on the attitude of serving all stakeholders and developing high levels of inclusiveness, gratitude and consciousness would lead to more happiness and superior results for all.</p>
  <p style="margin-top:21px">Our own purpose is to focus on these topics for the benefit of companies and leaders alike, thus creating an increased level of self-awareness, responsibility, fairness and alignment.</p>
  <p style="margin-top:21px">Seeing leaders and companies intensely passionate for what they engage in and achieving results beyond what has been thought possible fills us with joy and gives us great fulfilment.</p>
</div>

<div class="abs num" style="left:196px;top:1118px">01</div>
<h3 class="abs h-sub" style="left:203px;top:1172px">Who we are</h3>
<p class="abs body-m" style="left:207px;top:1242px;width:270px">Cobalt Sages was founded in 2017 by Matthias and Selina and incorporated in 2019 with Reto as President.</p>
<div class="abs photo" role="img" aria-label="Small figures arranged in a ring around a globe on a mint background" style="left:203px;top:1359px;width:339px;height:252px;background:radial-gradient(circle at 50% 50%,#6d9fb5 0,#6d9fb5 12%,#8fc7ad 30%,#7fd9bb 60%)"></div>
<div class="abs more" style="left:210px;top:1646px">Read more <svg width="16" height="12" viewBox="0 0 16 12"><path d="M1 6h13M9 1l5 5-5 5" fill="none" stroke="#111" stroke-width="1.3"/></svg></div>

<div class="abs num" style="left:671px;top:1396px">02</div>
<div class="abs photo" role="img" aria-label="Double exposure of a businessman silhouette and a city skyline" style="left:673px;top:1465px;width:309px;height:256px;background:linear-gradient(180deg,#dfe5ec,#b3bfcb 55%,#eef1f4)"></div>
<h3 class="abs h-sub" style="left:673px;top:1754px">Why we doit</h3>
<p class="abs body-m" style="left:676px;top:1825px;width:340px">We want to be instrumental in accelerating the transition to a thriving world and an enhanced level of meaning and happiness.</p>
<div class="abs more" style="left:673px;top:1918px">Read more <svg width="16" height="12" viewBox="0 0 16 12"><path d="M1 6h13M9 1l5 5-5 5" fill="none" stroke="#111" stroke-width="1.3"/></svg></div>

<div class="abs photo" role="img" aria-label="Hands joining blue and white puzzle pieces" style="left:221px;top:1956px;width:302px;height:444px;background:linear-gradient(150deg,#ddd5c8,#8fb3d6 50%,#2f5a8a 75%,#d7cfc2)"></div>
<div class="abs num" style="left:592px;top:2085px">03</div>
<h3 class="abs h-sub" style="left:601px;top:2152px">How we doit</h3>
<p class="abs body-m" style="left:604px;top:2221px;width:275px">We convert the speak of purpose and consciousness into concrete solutions. We offer our services to corporations and individuals and a special series of retreats to the wider public.</p>
<div class="abs more" style="left:604px;top:2377px">Read more <svg width="16" height="12" viewBox="0 0 16 12"><path d="M1 6h13M9 1l5 5-5 5" fill="none" stroke="#111" stroke-width="1.3"/></svg></div>

<h2 class="abs h-big" style="left:136px;top:2547px">Retreats in<br>Pontresina</h2>
<p class="abs" style="left:636px;top:2552px;width:430px;font-size:20px;line-height:28px">Several times per year, we organize retreats that focus on conscious leadership, defining one’s vision, purpose and legacy.</p>
<div class="abs more" style="left:641px;top:2669px">Read more <svg width="16" height="12" viewBox="0 0 16 12"><path d="M1 6h13M9 1l5 5-5 5" fill="none" stroke="#111" stroke-width="1.3"/></svg></div>
<div class="abs photo" role="img" aria-label="Misty mountain lake at dawn with a wooden jetty" style="left:145px;top:2734px;width:910px;height:355px;background:linear-gradient(180deg,#6f7560 0%,#b8bbb5 30%,#d9d9d4 50%,#9a9d93 70%,#4c5135 100%)"></div>

<h2 class="abs h-big" style="left:147px;top:3236px">Testimonials</h2>
<div class="abs" style="left:663px;top:3196px;display:flex;align-items:center;gap:7px;font-size:20px;color:var(--text)"><span style="width:14px;height:14px;border-radius:50%;background:var(--text)"></span>Northvale Systems</div>
<p class="abs" style="left:657px;top:3257px;width:395px;font-size:15.5px;line-height:20.5px">The Cobalt Sages team enabled me to discuss current and relevant topics in a safe setting, with the group acting as sparring partner and supporter to find solutions.</p>
<div class="abs" style="left:663px;top:3384px;font-size:12.5px;line-height:17px"><b style="font-weight:500">Lorena Abderhalt</b><br>Halden Bank, Head Wealth Planning</div>

<div class="abs rule"></div>
<h2 class="abs" style="left:0;width:1200px;top:3542px;text-align:center;font-size:32px;font-weight:400;color:var(--ink)">Media &amp; Press</h2>

<div class="abs photo" role="img" aria-label="Runner climbing outdoor concrete stairs" style="left:127px;top:3624px;width:276px;height:175px;background:linear-gradient(135deg,#d8d6d2,#a9a6a0 60%,#6e6b66)"></div>
<div class="abs" style="left:133px;top:3819px;width:270px">
  <div class="card-title">We published our first book</div>
  <div class="card-date">15. September 2020</div>
  <div class="card-text">We published our first book, the workbook for the Cobalt Sages Quest. Please get in touch if you are interested.</div>
</div>

<div class="abs photo" role="img" aria-label="Portrait photo of a senior banker" style="left:452px;top:3624px;width:278px;height:175px;background:linear-gradient(180deg,#e6e6e4,#c7c2bb 60%,#4a4d55)"></div>
<div class="abs" style="left:458px;top:3819px;width:272px">
  <div class="card-title">ehemaliger veltra-topmanager leitet «cobalt sages»</div>
  <div class="card-date">15. September 2020</div>
  <div class="card-text">An ex-Veltra private banker is taking over the reins of a network for top executives. The move comes as the Swiss-based club formalizes its structure and incorporates itself.</div>
</div>

<div class="abs photo" role="img" aria-label="Conference slide with speaker portraits on a dark blue background" style="left:790px;top:3624px;width:277px;height:175px;background:linear-gradient(180deg,#0e1a4a,#1d2f74 55%,#0c1640)"></div>
<div class="abs" style="left:796px;top:3819px;width:275px">
  <div class="card-title">Alpine Circle of MBAs: Digital Leaders Conference 2021.</div>
  <div class="card-date">15. September 2020</div>
  <div class="card-text">We published our first book, the workbook for the Cobalt Sages Quest. Please get in touch if you are interested.</div>
</div>

<svg class="abs" style="left:557px;top:4028px" width="80" height="12" viewBox="0 0 80 12">
  <circle cx="6" cy="6" r="4.5" fill="var(--dot-active)"/><circle cx="29" cy="6" r="4.5" fill="var(--dot)"/><circle cx="50" cy="6" r="4.5" fill="var(--dot)"/><circle cx="71" cy="6" r="4.5" fill="var(--dot)"/>
</svg>

<footer>
<div class="abs footer"></div>
<div class="abs" style="left:152px;top:4203px;display:flex;align-items:center;gap:30px;font-size:39px;color:var(--ink)">Get in Touch <svg width="30" height="26" viewBox="0 0 30 26"><path d="M1 13h26M16 2l11 11-11 11" fill="none" stroke="#111" stroke-width="2"/></svg></div>
<div class="abs foot-col" style="left:633px;top:4214px">Cobalt Sages Ltd.<br>Talweg 12<br>8001 Zurich<br>Telephone: +41 44 555 01 27<br>Email: info@cobaltsages.ch</div>
<div class="abs foot-col" style="left:915px;top:4214px">RETREATS<br>Cobalt Sages:<br>18.03.2022 – 19.03.2022<br>08.06.2022 – 11.06.2022<br>28.09.2022 – 01.10.2022<br><br>Clearpeak Retreats<br>02.03.2022 – 05.03.2022 (Level I)<br>14.09.2022 – 17.09.2022 (Level II)<br><br>Trail to Reconnect<br>16.06.2022 – 19.06.2022</div>
<div class="abs bar">© Copyright - Cobalt Sages</div>
</footer>
</body>
</html>
```